Brevant Business Card

I have a business that is called "Brevant Electrical Products LTD" My company deals with top of the range laptops and mobile phones that are exclusive. I need a business card that will be eye catching but not over complicated.

Target Market(s)

Adults aged 19 to 50
Upper middle class

Industry/Entity Type

Business

Requirements
Must have
• Company name/logo (file attached)
• It must have my contact information which is:

• Name: Dale Marwick

• Position: Managing Director 

• Business Address: 7 Hapton Row, London, W4 9QD

• Contact Number: 02085193604
• Mobile: 07814260537
• Email: info@brevant-goods.co.uk
Nice to have
• Simple and stylish
• Eye catching

```html
<!DOCTYPE html>
<html lang="en">
<head>
<meta charset="utf-8">
<title>Brevant Electrical Products – Business Card</title>
<link rel="stylesheet" href="https://fonts.googleapis.com/css2?family=Arimo:wght@400;700&family=Questrial&display=swap">
<style>
  :root {
    --card-white: #ffffff;
    --edge-grey: #c9c9c9;
    --ink: #1a1a1a;
    --brand-blue: #3aa7d8;
    --brand-deep: #2f6a86;
    --sweep-blue: #0a8bd8;
    --sweep-navy: #2b6d93;
  }
  * { margin: 0; padding: 0; box-sizing: border-box; }
  html, body {
    width: 1200px; height: 662px; overflow: hidden;
    background: var(--card-white);
  }
  .card {
    position: relative; width: 1200px; height: 662px; overflow: hidden;
    font-family: "Arimo", Arial, sans-serif; color: var(--ink);
  }
  .card-backdrop { position: absolute; inset: 0; width: 100%; height: 100%; }
  .holder { position: absolute; left: 130px; top: 66px; }
  .holder-name { font-size: 40px; font-weight: 400; line-height: 1; }
  .holder-role { font-size: 26px; margin-top: 10px; margin-left: 4px; line-height: 1; }
  .brand { position: absolute; left: 618px; top: 58px; color: var(--brand-blue); }
  .brand-name {
    font-family: "Questrial", Arial, sans-serif;
    font-size: 92px; font-weight: 400; letter-spacing: 6px; line-height: 1;
  }
  .brand-tagline {
    font-family: "Questrial", Arial, sans-serif;
    color: var(--brand-deep); font-size: 38px; letter-spacing: 2px;
    margin-top: 6px; line-height: 1;
  }
  .contact { position: absolute; left: 66px; top: 398px; list-style: none; }
  .contact li { font-size: 21px; line-height: 1; margin-bottom: 17px; white-space: nowrap; }
  .contact .contact-address { font-size: 25px; }
  .email {
    position: absolute; left: 88px; top: 574px;
    font-size: 22px; font-weight: 700; letter-spacing: 3px; color: #2a2a2a;
  }
</style>
</head>
<body>
  <main class="card">
    <svg class="card-backdrop" viewBox="0 0 1061 585" preserveAspectRatio="none" aria-hidden="true">
      <defs>
        <linearGradient id="edge-fade" x1="0" y1="0" x2="1" y2="0">
          <stop offset="0" stop-color="#bdbdbd"/>
          <stop offset="1" stop-color="#e6e6e6"/>
        </linearGradient>
        <linearGradient id="sweep-fill" x1="0" y1="0" x2="1" y2="1">
          <stop offset="0" stop-color="#1a9be0"/>
          <stop offset="1" stop-color="#0a7fcc"/>
        </linearGradient>
      </defs>
      <rect width="1061" height="585" fill="url(#edge-fade)"/>
      <ellipse cx="640" cy="300" rx="620" ry="370" fill="var(--card-white)"/>
      <path d="M690 0 L1061 0 L1061 585 L860 585 Q1045 420 1005 230 Q955 55 690 0 Z" fill="url(#sweep-fill)"/>
      <path d="M520 0 Q960 40 1061 215" fill="none" stroke="var(--card-white)" stroke-width="10"/>
      <path d="M530 6 Q950 50 1061 228" fill="none" stroke="var(--sweep-navy)" stroke-width="9"/>
      <path d="M1061 250 Q1075 430 900 585" fill="none" stroke="var(--card-white)" stroke-width="8"/>
    </svg>

    <header class="holder">
      <h1 class="holder-name">Dale Marwick</h1>
      <p class="holder-role">Managing Director</p>
    </header>

    <div class="brand">
      <p class="brand-name">BREVANT</p>
      <p class="brand-tagline">Electrical Products</p>
    </div>

    <ul class="contact">
      <li>business address : <span class="contact-address">7 HAPTON ROW ,LONDON,W4 9QD</span></li>
      <li>contact number:02085193604</li>
      <li>mobile:07814260537</li>
    </ul>

    <p class="email">email:info@brevant-goods.co.uk</p>
  </main>
</body>
</html>
```